Stationary and Business Card Design

We need a stationery design and a business card design for a non-profit economics development agency. Our website is growharborline.org. Our clients are Canadian government agencies and large Chinese company. We need the design to be professional and corporate.

Please see attached for our Power Point presentation. Please take design elements from our website and our ppt.

```html
<!DOCTYPE html>
<html lang="en">
<head>
<meta charset="utf-8">
<title>Harborline Growth Alliance – Business Card</title>
<link href="https://fonts.googleapis.com/css2?family=Open+Sans:wght@400;600;700&display=swap" rel="stylesheet">
<style>
  :root {
    --brand-red: #e2232f;
    --brand-red-dark: #c81a25;
    --ink: #2b2b2b;
    --ink-soft: #5a5a5a;
    --paper: #f4f4f4;
    --backdrop: #e6e4e1;
    --curve-black: #1c1c1c;
  }
  * { box-sizing: border-box; margin: 0; padding: 0; }
  html, body {
    width: 1200px; height: 900px; overflow: hidden;
    background: var(--backdrop);
    font-family: "Open Sans", Arial, sans-serif;
  }
  .canvas { position: relative; width: 1200px; height: 900px; }

  .card {
    position: absolute; width: 560px; height: 320px;
    border-radius: 4px; overflow: hidden;
    box-shadow: 0 10px 24px rgba(0,0,0,0.18);
  }

  /* Front of card */
  .card-front { left: 560px; top: 100px; background: var(--brand-red); }
  .front-leaf-area {
    position: absolute; left: 40px; top: -40px; width: 260px; height: 240px;
    border-radius: 50%;
    background: radial-gradient(circle, rgba(255,255,255,0.16) 0%, rgba(255,255,255,0.05) 60%, rgba(255,255,255,0) 72%);
  }
  .front-brand {
    position: absolute; left: 230px; top: 150px;
    display: flex; align-items: center; gap: 10px;
  }
  .brand-square { width: 18px; height: 18px; }
  .front-brand .brand-square { background: #ffffff; }
  .front-brand .brand-name {
    color: #ffffff; font-weight: 700; font-size: 21px; letter-spacing: 0.2px;
  }

  /* Back of card */
  .card-back { left: 80px; top: 470px; background: var(--paper); }
  .back-wave { position: absolute; left: 0; top: 0; width: 560px; height: 320px; }
  .back-leaf-area {
    position: absolute; left: 18px; top: 96px; width: 80px; height: 44px;
    border-radius: 22px;
    background: linear-gradient(90deg, #1f1f1f 0%, #444 55%, #9a9a9a 100%);
  }
  .back-brand {
    position: absolute; left: 40px; top: 42px;
    display: flex; align-items: center; gap: 8px;
  }
  .back-brand .brand-square { background: var(--brand-red); }
  .back-brand .brand-name {
    color: var(--brand-red); font-weight: 700; font-size: 19px;
  }

  .contact-block { position: absolute; left: 318px; top: 92px; color: var(--ink); }
  .person-name { color: var(--brand-red); font-weight: 700; font-size: 16px; }
  .person-title { color: var(--ink-soft); font-size: 13px; margin-bottom: 12px; }
  .org-name, .org-address { font-size: 12px; line-height: 18px; }
  .org-address { margin-bottom: 10px; }
  .contact-list { list-style: none; }
  .contact-list li {
    display: flex; align-items: center; gap: 10px;
    font-size: 12px; line-height: 19px;
  }
  .contact-icon { width: 11px; height: 11px; flex: none; }
  .contact-list .no-icon { padding-left: 21px; }
</style>
</head>
<body>
<main class="canvas">

  <section class="card card-front" aria-label="Business card front">
    <div class="front-leaf-area" role="img" aria-label="Large faint maple leaf decoration"></div>
    <div class="front-brand">
      <span class="brand-square"></span>
      <span class="brand-name">Harborline Growth Alliance</span>
    </div>
  </section>

  <section class="card card-back" aria-label="Business card back">
    <svg class="back-wave" viewBox="0 0 560 320" aria-hidden="true">
      <path d="M0 150 C 120 150, 170 240, 300 290 C 380 318, 470 320, 560 320 L 0 320 Z" fill="var(--brand-red)"/>
      <path d="M0 140 C 130 140, 180 230, 300 282 C 390 316, 480 318, 560 318" fill="none" stroke="var(--curve-black)" stroke-width="5"/>
    </svg>
    <div class="back-leaf-area" role="img" aria-label="Black and grey maple leaf decoration"></div>
    <div class="back-brand">
      <span class="brand-square"></span>
      <span class="brand-name">Harborline Growth Alliance</span>
    </div>

    <div class="contact-block">
      <p class="person-name">Mara Ellison</p>
      <p class="person-title">President</p>
      <p class="org-name">Harborline Growth Alliance</p>
      <p class="org-address">Harbour Lane 14 // 40210 canada</p>
      <ul class="contact-list">
        <li>
          <svg class="contact-icon" viewBox="0 0 12 12" aria-hidden="true"><path d="M2.5 1 L4.5 1 L5.3 3.6 L4 4.6 C4.6 6 6 7.4 7.4 8 L8.4 6.7 L11 7.5 L11 9.5 C11 10.3 10.3 11 9.5 11 C5 11 1 7 1 2.5 C1 1.7 1.7 1 2.5 1 Z" fill="var(--brand-red)"/></svg>
          +1 (0) 40 5550 1842
        </li>
        <li>
          <svg class="contact-icon" viewBox="0 0 12 12" aria-hidden="true"><rect x="3" y="0.5" width="6" height="11" rx="1.2" fill="var(--brand-red)"/><rect x="4" y="2" width="4" height="6.5" fill="#fff"/></svg>
          +1 (0) 151 5550 2376
        </li>
        <li>
          <svg class="contact-icon" viewBox="0 0 12 12" aria-hidden="true"><rect x="0.5" y="2" width="11" height="8" rx="1" fill="var(--brand-red)"/><path d="M1 2.6 L6 6.6 L11 2.6" fill="none" stroke="#fff" stroke-width="1"/></svg>
          mara@growharborline.org
        </li>
        <li class="no-icon">www.growharborline.org</li>
      </ul>
    </div>
  </section>

</main>
</body>
</html>
```